Bench Advertisement - We Buy Houses Design Needed

Need a catchy, simple but elegant design for bus benches to advertise our company.

We need our website, or phone number, and a smal description (1-2 bulletpoints of what we do and what we offer)

The tricky part is for the designer to fit everything and make the website name as part of the title and fitting everything so that people passing by on the street can see what we offer.

Our website is quickhomeofferhub.com - (916) 555-0142

Something simple but something that catches the eye of walking pedestrians, and drivers driving by the bench.

Our company buys houses, any condition, any situation, we buy houses for cash and close quickly. You can use this description to create a few bulletpoints however you like. Must follow dimensions in attachment.

Target Market(s)

People in foreclosure, about to lose their homes, people that need a quick cash sale of their property

Industry/Entity Type

Real Estate

Requirements
Must have
• catchy, website name, phone number, few brief bulletpoints about what we offer, colors that will catch peoples eye while walking or driving - advertisement will be placed on bus benches - visit our website to see the type of houses we buy - Also have more work for winner of design with possible bonuses
Nice to have
• Feel free to use description or images on our website - make sure the description is just bullet points and it fits with the overall theme / size of the advertisement - Bold bright colors - put yourself in their shoes (if you were going through financial difficulties and about to lose your house to foreclosure or auction, what would you want to see to pick up the phone and call us for a quick sale of your house?) (or if you have a house that you are having a problem with, problem renters, unkept/beat up house, what would make you want to call us and sell your house to us?)

```html
<!DOCTYPE html>
<html lang="en">
<head>
<meta charset="utf-8">
<title>Quick Home Offer Hub – Bench Advertisement</title>
<link href="https://fonts.googleapis.com/css2?family=Fira+Sans:wght@400;600;700&display=swap" rel="stylesheet">
<style>
  :root{
    --teal:#009595;
    --cloud:#ffffff;
    --cloud-shadow:#0d72a6;
    --ink-blue:#1a63ad;
    --white:#ffffff;
    --yellow:#fff200;
    --phone-red:#d6231c;
    --frame:#d9d9d9;
    --page:#ffffff;
  }
  html,body{margin:0;padding:0;overflow:hidden;}
  body{width:1200px;height:1200px;background:var(--page);font-family:"Fira Sans",sans-serif;}
  .canvas{position:relative;width:1198px;height:1198px;border:1px solid #bdbdbd;}
  .bench-ad{position:absolute;left:30px;width:1140px;height:325px;border:1px solid #f0f0f0;background:var(--page);}
  .bench-ad--top{top:150px;}
  .bench-ad--bottom{top:717px;}
  .bench-ad svg{position:absolute;left:12px;top:13px;width:1116px;height:298px;display:block;}
  .panel{fill:var(--teal);}
  .cloud-shadow{fill:var(--cloud-shadow);}
  .cloud-body{fill:var(--cloud);}
  .cloud-text{fill:var(--ink-blue);font-family:"Fira Sans",sans-serif;font-weight:600;text-anchor:middle;}
  .brand-name{fill:var(--white);font-family:"Fira Sans",sans-serif;font-weight:400;text-anchor:middle;letter-spacing:.3px;}
  .web-text{fill:var(--white);font-family:"Fira Sans",sans-serif;font-weight:600;}
  .phone-text{fill:var(--yellow);font-family:"Fira Sans",sans-serif;font-weight:600;}
  .globe{fill:none;stroke:var(--yellow);stroke-width:2;}
  .phone-badge{fill:var(--yellow);}
  .handset{fill:var(--phone-red);}
</style>
</head>
<body>
<div class="canvas">

  <svg width="0" height="0" style="position:absolute">
    <defs>
      <g id="cloud">
        <ellipse cx="0" cy="6" rx="62" ry="30"/>
        <circle cx="-34" cy="-6" r="26"/>
        <circle cx="8" cy="-16" r="32"/>
        <circle cx="40" cy="0" r="26"/>
        <circle cx="-50" cy="14" r="20"/>
        <circle cx="50" cy="18" r="20"/>
      </g>
      <g id="ad-content">
        <rect class="panel" x="0" y="0" width="1191" height="318"/>

        <!-- situation clouds -->
        <g transform="translate(117 106) scale(1.05 1.05)">
          <use href="#cloud" class="cloud-shadow" transform="translate(6 8)"/>
          <use href="#cloud" class="cloud-body"/>
        </g>
        <text class="cloud-text" font-size="22" x="124" y="101">Financial</text>
        <text class="cloud-text" font-size="22" x="124" y="123">Difficulties</text>

        <g transform="translate(313 66) scale(1.15 0.95)">
          <use href="#cloud" class="cloud-shadow" transform="translate(6 8)"/>
          <use href="#cloud" class="cloud-body"/>
        </g>
        <text class="cloud-text" font-size="21" x="320" y="62">Foreclosure</text>
        <text class="cloud-text" font-size="21" x="314" y="83">or Auction</text>

        <g transform="translate(514 104) scale(0.95 0.95)">
          <use href="#cloud" class="cloud-shadow" transform="translate(6 8)"/>
          <use href="#cloud" class="cloud-body"/>
        </g>
        <text class="cloud-text" font-size="26" x="522" y="97">Quick</text>
        <text class="cloud-text" font-size="26" x="522" y="123">Sale</text>

        <g transform="translate(730 92) scale(1.22 1.12)">
          <use href="#cloud" class="cloud-shadow" transform="translate(6 8)"/>
          <use href="#cloud" class="cloud-body"/>
        </g>
        <text class="cloud-text" font-size="27" x="732" y="78">Problem</text>
        <text class="cloud-text" font-size="27" x="732" y="104">Renters</text>

        <g transform="translate(977 92) scale(1.38 1.15)">
          <use href="#cloud" class="cloud-shadow" transform="translate(6 8)"/>
          <use href="#cloud" class="cloud-body"/>
        </g>
        <text class="cloud-text" font-size="21" x="974" y="82">Unkept/</text>
        <text class="cloud-text" font-size="21" x="987" y="107">beat up House</text>

        <!-- company name -->
        <text class="brand-name" font-size="25" x="248" y="245">QUICK HOME OFFER HUB</text>

        <!-- website -->
        <g transform="translate(478 198)">
          <circle class="globe" r="14"/>
          <ellipse class="globe" rx="6" ry="14"/>
          <line class="globe" x1="-14" y1="0" x2="14" y2="0"/>
          <line class="globe" x1="-12" y1="-7" x2="12" y2="-7"/>
          <line class="globe" x1="-12" y1="7" x2="12" y2="7"/>
        </g>
        <text class="web-text" font-size="37" x="502" y="211">www.quickhomeofferhub.com</text>

        <!-- phone -->
        <circle class="phone-badge" cx="560" cy="258" r="27"/>
        <path class="handset" d="M552 240 l7 -3 l5 11 l-5 4 c2 6 5 10 10 14 l4 -4 l10 7 l-3 6 c-4 3 -9 3 -13 0 c-9 -7 -15 -15 -18 -26 c-1 -4 0 -7 3 -9 z"/>
        <text class="phone-text" font-size="64" x="605" y="283">(916) 555-0142</text>
      </g>
    </defs>
  </svg>

  <section class="bench-ad bench-ad--top" aria-label="Bench advertisement, version one">
    <svg viewBox="0 0 1191 318" preserveAspectRatio="none">
      <use href="#ad-content"/>
    </svg>
  </section>

  <section class="bench-ad bench-ad--bottom" aria-label="Bench advertisement, version two">
    <svg viewBox="0 0 1191 318" preserveAspectRatio="none">
      <use href="#ad-content"/>
    </svg>
  </section>

</div>
</body>
</html>
```